CVA Business Card

I would like to create a busienss card for the high school teachers. Our school colors are red and black and our mascot is the bulldog. In addition, to our school address and contact information, I would like to add our twitter account and fb account. We also have a school website. Somewhere I would like to incorporate our school wide expectations: Be Safe, Be Respectful, Be Responsible and Be a Learner.

Thornbury Academy
2424 Pinegate
Thornbury, KS 67302
620.418.7093
620.418.7094(fax)
www.thornburylearning.example
www.facebook.example/ThornburyOtters
twitter.example/ThornburyKsDist or @ThornburyKsDist
Teacher Name:
Teacher Email:

I would like to personalize each card with the teacher name and their email.

I would also like to use Otter Circle – Roots.Now.Ahead

                                      Front Side of Card:  Teacher and School Contact Information

Back Side of Card:  Otter Circle -several designers have asked about this-our school is trying to promote that we are a family trying to promote a positive climate.  We also want to add Roots.Now.Ahead with information that might pertain to the past, present, or future to keep people coming back to our website or friendsnet.

At first I mentioned that I wanted to use the bulldog as the graphic because it is our mascot, now I am changing my mind about maybe something more student centered like a group of stick figures circle together or arms around each other symbolizing that we are working together to accomplish our goal.

I need to make sure that our school wide expectations are also incorporated:

Be Safe.Be Respectful.Be Responsible.Be A Learner

Target Market(s)

9-12 students and professionals

Industry/Entity Type

High School

Requirements
Must have
• Contact information
Otter Circle with Past, Present and Future Incorporated
Two sided business card
Side #1 Contact Info + graphic (might use bulldog that I attached however not sure if I like it)
Side #2 Otter Circle with Past, Present and Future (incorporate a graphic that symbolizes togetherness or working together.

```html
<!DOCTYPE html>
<html lang="en">
<head>
<meta charset="utf-8">
<title>Otter Circle – Teacher Card</title>
<link rel="stylesheet" href="https://fonts.googleapis.com/css2?family=Oswald:wght@300;400&family=Jost:wght@300;400&display=swap">
<style>
  :root {
    --red: #d3262b;
    --black: #000000;
    --white: #ffffff;
    --paper: #ffffff;
    --hand-light: #ececec;
    --hand-mid: #d9d9d9;
  }
  * { margin: 0; padding: 0; box-sizing: border-box; }
  html, body {
    width: 1200px; height: 857px; overflow: hidden;
    background: var(--paper);
  }
  .canvas { position: relative; width: 1200px; height: 857px; }

  .brand-title {
    position: absolute; left: 0; width: 1200px; top: 150px;
    text-align: center;
    font-family: "Oswald", sans-serif; font-weight: 400;
    font-size: 72px; line-height: 80px; letter-spacing: -0.5px;
    color: var(--red);
  }
  .brand-tagline {
    position: absolute; left: 0; width: 1200px; top: 226px;
    text-align: center;
    font-family: "Jost", sans-serif; font-weight: 400;
    font-size: 20px; line-height: 24px; letter-spacing: 0.45em;
    color: var(--black);
  }
  .brand-tagline .dot { color: var(--red); }

  .togetherness-art {
    position: absolute; left: 399px; top: 268px; width: 413px; height: 105px;
    background: linear-gradient(90deg, var(--hand-mid), var(--hand-light) 45%, var(--hand-light) 55%, var(--hand-mid));
    border-radius: 30px 30px 0 0;
  }

  .contact-card {
    position: absolute; left: 387px; top: 421px; width: 435px; height: 253px;
    background: var(--black); color: var(--white);
    text-align: center;
  }
  .teacher-name {
    position: absolute; left: 0; width: 100%; top: 18px;
    font-family: "Jost", sans-serif; font-weight: 400;
    font-size: 22px; line-height: 26px;
    letter-spacing: 0.33em; color: var(--red);
  }
  .contact-line {
    position: absolute; left: 0; width: 100%;
    font-family: "Oswald", sans-serif; font-weight: 400;
    font-size: 15px; line-height: 20px; color: var(--white);
    display: flex; justify-content: center; align-items: center; gap: 4px;
  }
  .contact-line svg { flex: none; fill: var(--white); }
  .school-name { top: 59px; }
  .address { top: 80px; }
  .phones { top: 100px; }
  .social { top: 137px; }
  .twitter { top: 157px; }
  .website { top: 176px; }
  .gap { display: inline-block; width: 6px; }
  .expectations {
    position: absolute; left: 0; width: 100%; top: 214px;
    font-family: "Oswald", sans-serif; font-weight: 300;
    font-size: 18px; line-height: 22px; color: var(--red);
  }
</style>
</head>
<body>
<main class="canvas">
  <h1 class="brand-title">OTTER CIRCLE</h1>
  <p class="brand-tagline">ROOTS <span class="dot">•</span> NOW <span class="dot">•</span> AHEAD</p>

  <div class="togetherness-art" role="img" aria-label="Row of six raised hands in soft grey, symbolising students working together"></div>

  <section class="contact-card">
    <h2 class="teacher-name">TEACHER’S NAME</h2>
    <p class="contact-line school-name">Thornbury Academy</p>
    <p class="contact-line address">
      <svg width="12" height="11" viewBox="0 0 12 11" aria-hidden="true"><path d="M6 0 L12 5.5 H10 V11 H7.3 V7.5 H4.7 V11 H2 V5.5 H0 Z"/></svg>
      2424 Pinegate, Thornbury, KS 67302
    </p>
    <p class="contact-line phones">
      <svg width="9" height="13" viewBox="0 0 9 13" aria-hidden="true"><path d="M2 0 L4 3.5 L2.8 4.8 C3.2 6.6 4.2 8.2 5.4 9.3 L6.8 8.3 L9 11.5 L7.2 13 C3.4 12 0.5 7 0.3 2 Z"/></svg>
      620.418.7093
      <span class="gap"></span>
      <svg width="16" height="12" viewBox="0 0 16 12" aria-hidden="true"><path d="M4 0 H11 V4 H15 A1 1 0 0 1 16 5 V12 H0 V5 A1 1 0 0 1 1 4 H4 Z M5 1 V4 H10 V1 Z M3 7 V10 H13 V7 Z"/></svg>
      620.418.7094 (fax)
    </p>
    <p class="contact-line social">
      <svg width="12" height="12" viewBox="0 0 12 12" aria-hidden="true"><rect width="12" height="12" rx="2"/></svg>
      www.friendsnet.example/ThornburyOtters
    </p>
    <p class="contact-line twitter">
      <svg width="11" height="11" viewBox="0 0 11 11" aria-hidden="true"><circle cx="5.5" cy="5.5" r="5.5"/></svg>
      @ThornburyKsDist
    </p>
    <p class="contact-line website">
      <svg width="10" height="10" viewBox="0 0 10 10" aria-hidden="true"><circle cx="5" cy="5" r="4.4" fill="none" stroke="#fff" stroke-width="1"/><path d="M0.6 5 H9.4 M5 0.6 V9.4" stroke="#fff" stroke-width="0.8"/></svg>
      www.thornburylearning.example
    </p>
    <p class="expectations">Be Safe. Be Respectful. Be Responsible. Be A Learner.</p>
  </section>
</main>
</body>
</html>
```